Brightfield Training Course Outline re-design

We are wanting to re-design our template for course outlines. Course outlines are provided to prospective students wanting to find out more information about a course. Our website was recently revamped so we would want the new course outlines to have a similar look and feel to our website: www.brightfieldtraining.com.au
I have attached a current course outline. All content from the current outline must come across to the new one. We want to appeal to adult students wanting to work with children. We emphasise flexible timeframes, easy-to-use online system, prompt and friendly support from a trainer. We want to inspire people to engage in education and change their lives. This is reflected in our motto - Study | Brightfield | Achieve.
Ideally, this will become a template for other course outlines, so if the file can be provided in PDF as well as an editable format it would be greatly appreciated.
The colour codes from our website are:
Aqua: #81c9bd
Grey: #939598
Blue: #000080
Looking forward to responses.
Happy to email any images or logos needed.

Target Market(s)

Mums with children wanting to re-enter the workforce

Requirements
Must have
• All content from current course outline must come across.
• Brightfield Training logo

```html
<!DOCTYPE html>
<html lang="en">
<head>
<meta charset="utf-8">
<title>Course Outline – Certificate III in Education Support</title>
<link href="https://fonts.googleapis.com/css2?family=Roboto:wght@400;500;700&display=swap" rel="stylesheet">
<style>
  :root {
    --aqua: #5fb8a9;
    --aqua-soft: #81c9bd;
    --grey: #939598;
    --grey-dark: #6d6e71;
    --blue: #1f1f7a;
    --paper: #f2f2f2;
    --backdrop: #b3b3b3;
  }
  * { margin: 0; padding: 0; box-sizing: border-box; }
  html, body {
    width: 1200px;
    height: 939px;
    overflow: hidden;
    background: var(--backdrop);
    font-family: "Roboto", Arial, sans-serif;
  }
  .cover {
    position: absolute;
    left: 300px;
    top: 26px;
    width: 600px;
    height: 886px;
    background: linear-gradient(90deg, #e6e6e6 0%, var(--paper) 3%, #f7f7f7 60%, #ededed 100%);
  }
  .brand {
    position: absolute;
    top: 76px;
    right: 40px;
    display: flex;
    align-items: center;
    gap: 10px;
    color: var(--blue);
    font-weight: 700;
    font-size: 22px;
    letter-spacing: -0.3px;
  }
  .brand-mark {
    width: 14px;
    height: 14px;
    background: var(--aqua-soft);
  }
  .title-block {
    position: absolute;
    left: 44px;
    top: 156px;
  }
  .doc-title {
    color: var(--aqua);
    font-weight: 500;
    font-size: 49px;
    line-height: 1;
    letter-spacing: -0.3px;
  }
  .course-name {
    margin-top: 14px;
    color: var(--grey-dark);
    font-weight: 700;
    font-size: 17px;
  }
  .course-code {
    margin-top: 3px;
    color: var(--grey);
    font-weight: 400;
    font-size: 17px;
  }
  .hero-band {
    position: absolute;
    left: 0;
    top: 311px;
    width: 600px;
    height: 449px;
    display: block;
  }
  .copyright {
    position: absolute;
    left: 0;
    right: 0;
    top: 790px;
    text-align: center;
    color: var(--grey-dark);
    font-weight: 500;
    font-size: 12px;
  }
</style>
</head>
<body>
  <main class="cover">
    <div class="brand"><span class="brand-mark"></span>Brightfield Training</div>

    <header class="title-block">
      <h1 class="doc-title">Course Outline</h1>
      <p class="course-name">Certificate III in Education Support</p>
      <p class="course-code">CHC30213</p>
    </header>

    <svg class="hero-band" viewBox="0 0 440 329" preserveAspectRatio="none">
      <defs>
        <linearGradient id="photoTones" x1="0" y1="0" x2="1" y2="1">
          <stop offset="0" stop-color="#cfd3d4"/>
          <stop offset="0.35" stop-color="#c79a74"/>
          <stop offset="0.7" stop-color="#b9a37a"/>
          <stop offset="1" stop-color="#d9b561"/>
        </linearGradient>
      </defs>
      <rect class="hero-photo" x="0" y="0" width="440" height="329" fill="url(#photoTones)" role="img" aria-label="Photo of a teacher and a young boy working together at a laptop in a classroom"/>
      <path class="accent-aqua" d="M352 0 L412 0 L296 290 L280 250 Z" fill="var(--aqua-soft)"/>
      <path class="accent-blue" d="M412 0 Q420 0 440 2 L440 329 L284 329 Q272 329 277 316 Z" fill="var(--blue)"/>
    </svg>

    <p class="copyright">© 2016 Copyright Brightfield Training</p>
  </main>
</body>
</html>
```